Stationery Design Project for Marketing Consultancy

I have started a new consultancy business and require the following elements to be designed using existing logo:
• Business card
• Letterhead
• Envelope (DL, C4, C5)
• Microsoft word template for report writing
• A4 Presentation Folder
• Powerpoint template
COPY FOR FRONT AND BACK OF BUSINESS CARD
logo
'Countable Growth. Bold Outcomes' slogan (but no need to use existing lockup with logo)
name, B Bus. Mktg, Grad Dip Digital Mktg, CPM (post nominal abbreviations in smaller font)
mobile: 04XX-XXX-XXX (I will give details to the winner to add)
website: www.quorvale.com.au
email: info@quorvale.com.au
COPY FOR LETTERHEAD
Logo
Company Name
Please, submit your designs that include business card, letterhead and envelope. Once selected the winner will be asked to complete the project by creating the rest of the artwork.
FINAL FILES
Print ready files to be supplied as well as Indesign files so that minor amends can be made if necessary in future.
• Layered vectors in EPS & PDF
• Screen quality JPEG & PNGs
ABOUT THE BUSINESS: QUORVALE
I work with clients to understand their business challenges, developing and executing measurable marketing strategies tied to key business metrics. Services include:
Services include:
• Business planning and business development
• Marketing and brand strategy
• Insight-driven integrated campaigns
• Loyalty programs and retention marketing
• Marketing automation
• Direct marketing (traditional and digital)
• Content strategy and development
Hi everyone,
Target Market(s)
Corporate decision makers (heads of marketing, general managers etc) and small to medium sized business owners. Predominately male aged 35+
Industry/Entity Type
Marketing
Requirements
Must have
- BRAND PERSONALITY
The successful design will communicate brand personality. I am a professional, results-driven entrepreneur, but want to show off my creative flair.
MEMORABILITY
Looking for a unique and eye-catching design. Am considering special printing effects (die cuts, letterpress, interactive elements, embossing, foiling etc) or a striking minimalist approach.
Nice to have
- I have a mission that could be incorporated on reverse if room -
Turning insights into actions & passion into profit.
Should not have
- Use of pink or green.

```html
<!DOCTYPE html>
<html lang="en">
<head>
<meta charset="utf-8">
<title>Quorvale Stationery</title>
<link href="https://fonts.googleapis.com/css2?family=Open+Sans:wght@400;600;800&display=swap" rel="stylesheet">
<style>
  :root{
    --canvas:#efede8;
    --gold:#e0b400;
    --gold-deep:#c99f00;
    --slate:#58585a;
    --slate-dark:#3f3f41;
    --ink:#2e2e30;
    --paper:#ffffff;
    --white:#ffffff;
  }
  *{box-sizing:border-box;margin:0;padding:0}
  html,body{width:1200px;height:900px;overflow:hidden}
  body{background:var(--canvas);font-family:"Open Sans",Arial,sans-serif;position:relative}

  .piece{position:absolute;overflow:hidden;box-shadow:0 2px 8px rgba(0,0,0,.18)}

  .wordmark{font-weight:800;letter-spacing:.02em;color:var(--ink);line-height:1}
  .slogan{font-weight:600;text-transform:uppercase;letter-spacing:.06em;color:var(--ink);line-height:1}

  /* Envelope front */
  .envelope-front{left:40px;top:40px;width:520px;height:260px;background:var(--slate)}
  .envelope-front .wordmark{position:absolute;left:30px;top:30px;font-size:28px}
  .envelope-front .slogan{position:absolute;left:31px;top:64px;font-size:8px}
  .diecut{position:absolute;border-radius:50%;background:var(--gold)}
  .envelope-front .diecut{width:170px;height:170px;right:-40px;bottom:-70px}

  /* Envelope back */
  .envelope-back{left:40px;top:320px;width:520px;height:260px;background:var(--gold)}
  .envelope-back .flap{position:absolute;left:0;top:0;width:100%;height:74px}
  .contact-line{position:absolute;left:22px;bottom:22px;display:flex;align-items:center;gap:6px;color:var(--white);font-size:8.5px;font-weight:600;white-space:nowrap}
  .contact-line .person{font-size:11px;font-weight:800}
  .contact-line svg{width:9px;height:9px;flex:none}
  .mini-mark{position:absolute;right:22px;bottom:22px;font-size:9px;font-weight:800;color:var(--ink);letter-spacing:.02em;line-height:1}

  /* Letterhead front */
  .letterhead{left:600px;top:40px;width:270px;height:382px;background:var(--paper)}
  .letterhead .wordmark{position:absolute;left:22px;top:24px;font-size:20px}
  .letterhead .slogan{position:absolute;left:23px;top:48px;font-size:5.5px}
  .letterhead .footer-rule{position:absolute;left:0;right:18px;bottom:26px;height:4px;background:var(--gold)}
  .letterhead .footer-rule.thin{bottom:20px;height:1.5px}
  .letterhead .footer-block{position:absolute;right:6px;bottom:20px;width:9px;height:10px;background:var(--slate)}

  /* Letterhead reverse */
  .letterhead-back{left:890px;top:40px;width:270px;height:382px;background:var(--gold)}
  .letterhead-back .contact-line{left:12px;bottom:16px;font-size:5px;gap:3px}
  .letterhead-back .contact-line .person{font-size:7px}
  .letterhead-back .contact-line svg{width:5px;height:5px}
  .letterhead-back .mini-mark{right:12px;bottom:30px;font-size:7px}

  /* Business cards */
  .card{top:620px;width:420px;height:240px;border-radius:18px}
  .card-front{left:170px;background:var(--slate)}
  .card-front .wordmark{position:absolute;left:28px;top:28px;font-size:30px}
  .card-front .slogan{position:absolute;left:29px;top:63px;font-size:8px}
  .card-front .diecut{width:150px;height:150px;right:-30px;top:-60px}
  .card-front .holder{position:absolute;left:28px;top:98px;color:var(--white)}
  .holder .name{font-size:17px;font-weight:800;line-height:1.1}
  .holder .postnominals{font-size:8px;font-weight:400;margin-top:3px}
  .contact-list{list-style:none;margin-top:10px}
  .contact-list li{display:flex;align-items:center;gap:7px;font-size:11px;font-weight:600;line-height:1.45}
  .contact-list svg{width:11px;height:11px}

  .card-back{left:610px;background:var(--gold)}
  .card-back .diecut{background:var(--slate-dark);width:160px;height:160px;left:-50px;bottom:-80px}
  .card-back .mini-mark{right:auto;left:250px;top:34px;bottom:auto;font-size:10px}
</style>
</head>
<body>

  <!-- DL envelope, front -->
  <section class="piece envelope-front" aria-label="Envelope front">
    <div class="wordmark">QUORVALE</div>
    <div class="slogan">Countable Growth. Bold Outcomes.</div>
    <div class="diecut" role="img" aria-label="Gold die-cut brand shape"></div>
  </section>

  <!-- DL envelope, back -->
  <section class="piece envelope-back" aria-label="Envelope back">
    <svg class="flap" viewBox="0 0 520 74" preserveAspectRatio="none" aria-hidden="true">
      <polygon points="0,0 520,0 520,62 508,74 12,74 0,62" fill="var(--slate)"/>
    </svg>
    <div class="contact-line">
      <span class="person">Daniel Rourke</span>
      <svg viewBox="0 0 10 10"><circle cx="5" cy="5" r="4.5" fill="none" stroke="#fff"/><rect x="3.6" y="2.4" width="2.8" height="5.2" rx=".5" fill="#fff"/></svg>
      <span>04XX-XXX-XXX</span>
      <svg viewBox="0 0 10 10"><circle cx="5" cy="5" r="4.5" fill="none" stroke="#fff"/><ellipse cx="5" cy="5" rx="1.8" ry="3.6" fill="none" stroke="#fff" stroke-width=".8"/><line x1="1" y1="5" x2="9" y2="5" stroke="#fff" stroke-width=".8"/></svg>
      <span>www.quorvale.com.au</span>
      <svg viewBox="0 0 10 10"><circle cx="5" cy="5" r="4.5" fill="none" stroke="#fff"/><rect x="2.5" y="3.2" width="5" height="3.6" fill="none" stroke="#fff" stroke-width=".8"/><polyline points="2.5,3.2 5,5.2 7.5,3.2" fill="none" stroke="#fff" stroke-width=".8"/></svg>
      <span>info@quorvale.com.au</span>
    </div>
    <div class="mini-mark">QUORVALE</div>
  </section>

  <!-- Letterhead -->
  <section class="piece letterhead" aria-label="Letterhead">
    <div class="wordmark">QUORVALE</div>
    <div class="slogan">Countable Growth. Bold Outcomes.</div>
    <div class="footer-rule"></div>
    <div class="footer-rule thin"></div>
    <div class="footer-block"></div>
  </section>

  <!-- Letterhead reverse -->
  <section class="piece letterhead-back" aria-label="Letterhead reverse">
    <div class="contact-line">
      <span class="person">Daniel Rourke</span>
      <svg viewBox="0 0 10 10"><circle cx="5" cy="5" r="4.5" fill="none" stroke="#fff"/><rect x="3.6" y="2.4" width="2.8" height="5.2" rx=".5" fill="#fff"/></svg>
      <span>04XX-XXX-XXX</span>
      <svg viewBox="0 0 10 10"><circle cx="5" cy="5" r="4.5" fill="none" stroke="#fff"/><ellipse cx="5" cy="5" rx="1.8" ry="3.6" fill="none" stroke="#fff" stroke-width=".8"/><line x1="1" y1="5" x2="9" y2="5" stroke="#fff" stroke-width=".8"/></svg>
      <span>www.quorvale.com.au</span>
      <svg viewBox="0 0 10 10"><circle cx="5" cy="5" r="4.5" fill="none" stroke="#fff"/><rect x="2.5" y="3.2" width="5" height="3.6" fill="none" stroke="#fff" stroke-width=".8"/><polyline points="2.5,3.2 5,5.2 7.5,3.2" fill="none" stroke="#fff" stroke-width=".8"/></svg>
      <span>info@quorvale.com.au</span>
    </div>
    <div class="mini-mark">QUORVALE</div>
  </section>

  <!-- Business card, front -->
  <section class="piece card card-front" aria-label="Business card front">
    <div class="wordmark">QUORVALE</div>
    <div class="slogan">Countable Growth. Bold Outcomes.</div>
    <div class="diecut" role="img" aria-label="Gold die-cut brand shape"></div>
    <div class="holder">
      <div class="name">Daniel Rourke</div>
      <div class="postnominals">B Bus. Mktg, Grad Dip Digital Mktg, CPM</div>
      <ul class="contact-list">
        <li><svg viewBox="0 0 10 10"><circle cx="5" cy="5" r="4.5" fill="none" stroke="#fff"/><rect x="3.6" y="2.4" width="2.8" height="5.2" rx=".5" fill="#fff"/></svg>04XX-XXX-XXX</li>
        <li><svg viewBox="0 0 10 10"><circle cx="5" cy="5" r="4.5" fill="none" stroke="#fff"/><ellipse cx="5" cy="5" rx="1.8" ry="3.6" fill="none" stroke="#fff" stroke-width=".8"/><line x1="1" y1="5" x2="9" y2="5" stroke="#fff" stroke-width=".8"/></svg>www.quorvale.com.au</li>
        <li><svg viewBox="0 0 10 10"><circle cx="5" cy="5" r="4.5" fill="none" stroke="#fff"/><rect x="2.5" y="3.2" width="5" height="3.6" fill="none" stroke="#fff" stroke-width=".8"/><polyline points="2.5,3.2 5,5.2 7.5,3.2" fill="none" stroke="#fff" stroke-width=".8"/></svg>info@quorvale.com.au</li>
      </ul>
    </div>
  </section>

  <!-- Business card, back -->
  <section class="piece card card-back" aria-label="Business card back">
    <div class="diecut" role="img" aria-label="Dark die-cut brand shape"></div>
    <div class="mini-mark">QUORVALE</div>
  </section>

</body>
</html>
```